フルーツの材料を使った丸っこい、ゼリー&羊羹のシリーズを今後継続的に作っていく予定です。 それに合わせて、袋や箱に使用するラベルのデザインをお願いします。

フルーツ ぶどう、キウイ、すもも、もも、ブルーベリー、柿等

使用予定のフルーツは様々ありますので、統一して使えるラベルを希望しています。

名前のは「さやめのつぶ」を予定しています。

現在、予定しているのは添付ファイルにある、ゴム風船の中に入っているまるっこいかたちをした商品です。これは羊羹でもゼリーでも同じ形になります。
色は、使うフルーツの素材の色が分かる程度には分かります。

つまようじで、プッチとゴムを割って食べる楽しさも伝わるといいかなと考えてます。ゴムが光に弱く劣化しやすいために、外からは製品があまり見えないためです。
添付写真がついてません、申し訳ありませんでした。コロッとした可愛いやつなので、どうぞよろしくお願いします。 玉羊羹、丸羊羹をイメージしていただけるわかりやすいかと思います。

商品が並んだ時に、色から興味を持ってもらえそうで、「さやめ」という文字が目に入りやすい点からも選びました。

こんなに多くの提案が来るとは思っておらず、次点ももっとつけたかったぐらいです。また、売り方のPOPなどの参考にもなりました。ありがとうございます。
こちらかの説明も足りておらず、丸のゴム風船の商品にそのまま貼ることを想定させてしまったようで申し訳なかったです。
しかし、3個入りの商品など今後、展開が増えていけばまたお願いしたいと思います。

```html
<!DOCTYPE html>
<html lang="ja">
<head>
<meta charset="utf-8">
<title>さやめのつぶ ラベル展開</title>
<link rel="stylesheet" href="https://fonts.googleapis.com/css2?family=M+PLUS+Rounded+1c:wght@500;700&display=swap">
<style>
  :root {
    --paper: #ffffff;
    --crescent: #ffffff;
    --mark-text: #ffffff;
    --seal: #e6b9cf;
    --grape-a: #b47cc0; --grape-b: #7f4590;
    --plum-a: #f08cba; --plum-b: #d2457f;
    --kiwi-a: #b5cc74; --kiwi-b: #7f9c3a;
    --blueberry-a: #8a5a9a; --blueberry-b: #4d2660;
    --peach-a: #f3a6dc; --peach-b: #d66bb5;
    --persimmon-a: #f4c08a; --persimmon-b: #de8a4b;
  }
  html, body {
    margin: 0; padding: 0;
    width: 849px; height: 1200px;
    overflow: hidden;
    background: var(--paper);
  }
  .sheet { position: relative; width: 849px; height: 1200px; }
  .label {
    position: absolute;
    width: 298px; height: 200px;
    font-family: "M PLUS Rounded 1c", sans-serif;
  }
  .label svg { position: absolute; inset: 0; width: 100%; height: 100%; }
  .label__name {
    position: absolute;
    left: 38px; top: 50px;
    font-size: 19px; font-weight: 700; line-height: 24px;
    color: var(--mark-text);
    letter-spacing: 1px;
    white-space: nowrap;
  }
  .label__seal {
    position: absolute;
    left: 128px; top: 56px;
    width: 60px; height: 60px;
    border-radius: 50%;
    background: var(--seal);
  }
  .label__fruit {
    position: absolute;
    left: 190px; top: 126px;
    font-size: 12px; font-weight: 700;
    white-space: nowrap;
  }
  .label--grape { left: 98px; top: 183px; }
  .label--plum { left: 452px; top: 183px; }
  .label--kiwi { left: 98px; top: 494px; }
  .label--blueberry { left: 452px; top: 494px; }
  .label--peach { left: 98px; top: 834px; }
  .label--persimmon { left: 452px; top: 834px; }
  .label--grape .label__fruit { color: var(--grape-b); }
  .label--plum .label__fruit { color: var(--plum-b); }
  .label--kiwi .label__fruit { color: var(--kiwi-b); }
  .label--blueberry .label__fruit { color: var(--blueberry-b); left: 172px; }
  .label--peach .label__fruit { color: var(--peach-b); }
  .label--persimmon .label__fruit { color: var(--persimmon-b); }
</style>
</head>
<body>
<main class="sheet">
  <svg width="0" height="0" style="position:absolute">
    <defs>
      <clipPath id="oval-clip"><ellipse cx="149" cy="100" rx="147" ry="98"/></clipPath>
      <linearGradient id="g-grape" x1="0" y1="0" x2="1" y2="1"><stop offset="0" stop-color="var(--grape-a)"/><stop offset="1" stop-color="var(--grape-b)"/></linearGradient>
      <linearGradient id="g-plum" x1="0" y1="0" x2="1" y2="1"><stop offset="0" stop-color="var(--plum-a)"/><stop offset="1" stop-color="var(--plum-b)"/></linearGradient>
      <linearGradient id="g-kiwi" x1="0" y1="0" x2="1" y2="1"><stop offset="0" stop-color="var(--kiwi-a)"/><stop offset="1" stop-color="var(--kiwi-b)"/></linearGradient>
      <linearGradient id="g-blueberry" x1="0" y1="0" x2="1" y2="1"><stop offset="0" stop-color="var(--blueberry-a)"/><stop offset="1" stop-color="var(--blueberry-b)"/></linearGradient>
      <linearGradient id="g-peach" x1="0" y1="0" x2="1" y2="1"><stop offset="0" stop-color="var(--peach-a)"/><stop offset="1" stop-color="var(--peach-b)"/></linearGradient>
      <linearGradient id="g-persimmon" x1="0" y1="0" x2="1" y2="1"><stop offset="0" stop-color="var(--persimmon-a)"/><stop offset="1" stop-color="var(--persimmon-b)"/></linearGradient>
    </defs>
  </svg>

  <section class="label label--grape">
    <svg viewBox="0 0 298 200">
      <ellipse cx="149" cy="100" rx="147" ry="98" fill="url(#g-grape)" role="img" aria-label="ブドウ色の果肉のようなテクスチャ"/>
      <ellipse cx="190" cy="150" rx="150" ry="78" fill="var(--crescent)" clip-path="url(#oval-clip)"/>
    </svg>
    <div class="label__name">さやめの<br>つぶ</div>
    <div class="label__seal"></div>
    <div class="label__fruit">ブドウ</div>
  </section>

  <section class="label label--plum">
    <svg viewBox="0 0 298 200">
      <ellipse cx="149" cy="100" rx="147" ry="98" fill="url(#g-plum)" role="img" aria-label="スモモ色の果肉のようなテクスチャ"/>
      <ellipse cx="190" cy="150" rx="150" ry="78" fill="var(--crescent)" clip-path="url(#oval-clip)"/>
    </svg>
    <div class="label__name">さやめの<br>つぶ</div>
    <div class="label__seal"></div>
    <div class="label__fruit">スモモ</div>
  </section>

  <section class="label label--kiwi">
    <svg viewBox="0 0 298 200">
      <ellipse cx="149" cy="100" rx="147" ry="98" fill="url(#g-kiwi)" role="img" aria-label="キウイ色の果肉のようなテクスチャ"/>
      <ellipse cx="190" cy="150" rx="150" ry="78" fill="var(--crescent)" clip-path="url(#oval-clip)"/>
    </svg>
    <div class="label__name">さやめの<br>つぶ</div>
    <div class="label__seal"></div>
    <div class="label__fruit">キウイ</div>
  </section>

  <section class="label label--blueberry">
    <svg viewBox="0 0 298 200">
      <ellipse cx="149" cy="100" rx="147" ry="98" fill="url(#g-blueberry)" role="img" aria-label="ブルーベリー色の果肉のようなテクスチャ"/>
      <ellipse cx="190" cy="150" rx="150" ry="78" fill="var(--crescent)" clip-path="url(#oval-clip)"/>
    </svg>
    <div class="label__name">さやめの<br>つぶ</div>
    <div class="label__seal"></div>
    <div class="label__fruit">ブルーベリー</div>
  </section>

  <section class="label label--peach">
    <svg viewBox="0 0 298 200">
      <ellipse cx="149" cy="100" rx="147" ry="98" fill="url(#g-peach)" role="img" aria-label="モモ色の果肉のようなテクスチャ"/>
      <ellipse cx="190" cy="150" rx="150" ry="78" fill="var(--crescent)" clip-path="url(#oval-clip)"/>
    </svg>
    <div class="label__name">さやめの<br>つぶ</div>
    <div class="label__seal"></div>
    <div class="label__fruit">モモ</div>
  </section>

  <section class="label label--persimmon">
    <svg viewBox="0 0 298 200">
      <ellipse cx="149" cy="100" rx="147" ry="98" fill="url(#g-persimmon)" role="img" aria-label="カキ色の果肉のようなテクスチャ"/>
      <ellipse cx="190" cy="150" rx="150" ry="78" fill="var(--crescent)" clip-path="url(#oval-clip)"/>
    </svg>
    <div class="label__name">さやめの<br>つぶ</div>
    <div class="label__seal"></div>
    <div class="label__fruit">カキ</div>
  </section>
</main>
</body>
</html>
```